ROLVEN CHICKEN delivery menu

NEED A TAKEAWAY MENU FOR A FAST FOOD TAKEAWAY WITH PICTURES
THE BUSINESS IS CALLED ROLVEN CHICKEN
COLOURS LIKED ARE BLUE RED BLACK AND GREEN. THIS LEAFLET NEEDS TO BE A3 FOLDED AND AIMED AT DELIVERY

Target Market(s)

consumers of fried chicken, pizza etc

Industry/Entity Type

Business

Font styles to use
Serif
Sans Serif

Colors
ec1f27
0355a3
9ccb3b

Requirements
Must have
• pictures of fried chicken, burgers, pizza and kebabs and any other that will fit
Nice to have
• like a Marbrook grilled hen menu

```html
<!DOCTYPE html>
<html lang="en">
<head>
<meta charset="utf-8">
<title>Rolven Chicken – Delivery Menu</title>
<link href="https://fonts.googleapis.com/css2?family=Lilita+One&family=Arimo:ital,wght@0,400;0,700;1,400&display=swap" rel="stylesheet">
<style>
:root{
  --red:#e9222b;
  --red-deep:#d81e26;
  --white:#ffffff;
  --ink:#1a1a1a;
  --mint:#e3efd4;
  --cream:#fbfcf7;
  --sand:#e8c3a7;
  --stage:#e4e4e4;
}
*{margin:0;padding:0;box-sizing:border-box}
html,body{width:1016px;height:1200px;overflow:hidden;background:var(--stage)}
body{position:relative;font-family:"Arimo",Arial,sans-serif;color:var(--ink)}
.sheet{position:absolute;left:159px;width:698px;height:493px;overflow:hidden;box-shadow:0 2px 8px rgba(0,0,0,.18)}
.sheet--outer{top:86px}
.sheet--inner{top:619px}
.panel{position:absolute;top:0;width:233px;height:100%}
.panel--1{left:0}.panel--2{left:233px}.panel--3{left:466px}
.panel--pale{background:linear-gradient(90deg,var(--mint) 0%,var(--cream) 100%)}
.panel--pale-r{background:linear-gradient(90deg,var(--cream) 0%,var(--mint) 100%)}
.panel--red{background:var(--red)}
.panel--red-fold{background:var(--red-deep);box-shadow:inset 3px 0 4px rgba(0,0,0,.08)}
.tag{position:absolute;background:var(--red);color:var(--white);font-family:"Lilita One",Impact,sans-serif;font-size:14px;letter-spacing:.8px;padding:3px 7px 2px;transform:rotate(-2deg);white-space:nowrap}
.tag-note{position:absolute;font-family:"Lilita One",Impact,sans-serif;font-size:5.4px;letter-spacing:.4px;color:var(--red);line-height:1.15;transform:rotate(-2deg);white-space:nowrap}
.abs{position:absolute}
.rule{border-left:1.6px solid var(--red);padding-left:4px}
.deal{position:absolute;left:20px;width:200px}
.deal .name{font-size:7.2px}
.deal .desc{font-size:3.9px;font-style:italic;color:var(--red);line-height:1.3;width:130px}
.deal .price{position:absolute;right:4px;top:0;font-size:9px;font-weight:700}
.row{position:absolute;font-size:5.4px;white-space:nowrap}
.row .p{position:absolute;font-weight:700;font-size:4.8px}
.sides .row{font-size:5px}
.item{position:absolute;width:210px}
.item .name{font-size:6.8px}
.item .desc{font-size:3.8px;font-style:italic;color:var(--red);line-height:1.3;width:115px}
.item .ps{position:absolute;top:0;font-weight:700;font-size:5.2px}
.item .pl{position:absolute;top:-1px;font-weight:700;font-size:8.6px}
.col-head{position:absolute;font-style:italic;color:var(--red);font-size:5px}
.flame{position:absolute;border-radius:50% 50% 18% 18% / 70% 70% 20% 20%}
.cover-name{position:absolute;left:30px;top:68px;width:172px;text-align:center;color:var(--white);font-family:"Lilita One",Impact,sans-serif;font-size:34px;letter-spacing:2px}
.cover-mark{position:absolute;left:94px;top:18px;width:46px;height:46px;border-radius:50%;background:var(--white)}
.cover-title{position:absolute;left:30px;top:262px;color:var(--white);font-family:"Lilita One",Impact,sans-serif;transform:rotate(-9deg);transform-origin:left top;text-align:center}
.cover-title .big{font-size:21px;letter-spacing:1px}
.cover-title .small{font-size:11px;letter-spacing:.6px;line-height:1}
.cover-info{position:absolute;left:0;width:233px;text-align:center;color:var(--white);font-family:"Lilita One",Impact,sans-serif;letter-spacing:.8px}
</style>
</head>
<body>

<!-- OUTSIDE SHEET -->
<section class="sheet sheet--outer">
  <div class="panel panel--1 panel--pale">
    <div class="tag" style="left:22px;top:42px">MEAL DEALS</div>
    <div class="deal rule" style="top:90px"><div class="name">Chicken Dinner Meal</div><div class="desc">2 Pieces of chicken, regular fries &amp; beans or coleslaw or a can of soft drink</div><div class="price">5.50 £</div></div>
    <div class="deal rule" style="top:116px"><div class="name">Fillet Burger Meal</div><div class="desc">Chicken fillet burger, regular fries &amp; a can of soft drink</div><div class="price">5.50 £</div></div>
    <div class="deal rule" style="top:136px"><div class="name">Quarter Pounder Meal</div><div class="desc">Quarter pounder burger, regular fries &amp; a can of soft drink</div><div class="price">5.50 £</div></div>
    <div class="deal rule" style="top:156px"><div class="name">BBQ Spare Ribs Meal</div><div class="desc">Portion of ribs, regular fries &amp; a can of soft drink</div><div class="price">5.50 £</div></div>
    <div class="deal rule" style="top:175px"><div class="name">Full House</div><div class="desc">Portion of ribs, 1 piece of chicken, regular fries &amp; a can of soft drink</div><div class="price">6.00 £</div></div>
    <div class="deal rule" style="top:195px"><div class="name">Chicken Variety Meal</div><div class="desc">2 Pieces of chicken, 2 hot wings, regular fries &amp; a can of soft drink</div><div class="price">5.50 £</div></div>
    <div class="deal rule" style="top:215px"><div class="name">Chicken Wrap Meal</div><div class="desc">Chicken fillet wrap, regular fries &amp; a can of soft drink</div><div class="price">5.50 £</div></div>
    <div class="deal rule" style="top:235px"><div class="name">Doner Wrap Meal</div><div class="desc">Lamb doner wrap, regular fries &amp; a can of soft drink</div><div class="price">5.50 £</div></div>
    <div class="deal rule" style="top:254px"><div class="name">Family Meal</div><div class="desc">12 Pieces of chicken, 4 fries, coleslaw, beans, corn on the cob &amp; a 1.5L bottle of drink</div><div class="price">17.00 £</div></div>
    <div class="deal rule" style="top:280px"><div class="name">Pizza Deal I</div><div class="desc">2 x 10 any pizza, 2 garlic torpedo with cheese, 10 Nuggets, Garlic Mushrooms, 1.5ltr bottle of soft drink</div><div class="price">23.00 £</div></div>
    <div class="deal rule" style="top:306px"><div class="name">Pizza Deal II</div><div class="desc">2 x 10 any pizza, 2 garlic torpedo with cheese, onion rings, 1.5ltr bottle of soft drink</div><div class="price">16.00 £</div></div>
    <div class="deal rule" style="top:332px"><div class="name">Kebab Deal</div><div class="desc">2 x large doner kebabs, 2 x chips, onion rings, 2 x cans of soft drink</div><div class="price">14.00 £</div></div>
    <div class="deal rule" style="top:352px"><div class="name">Boneles Chicken Deal</div><div class="desc">6 chicken fillet, 10 Nuggets, 1 portion of popcorn chicken, 1 portion of spicy chicken bites, 4 small chips, 1.5ltr bottle of drink</div><div class="price">19.00 £</div></div>
    <div class="deal rule" style="top:378px"><div class="name">Kids Meal</div><div class="desc">Popcorn chicken with chips and a can of soft drink or 4 chicken nuggets with chips and a can of soft drink</div><div class="price">3.40 £</div></div>
    <div class="flame" role="img" aria-label="Small red flame decoration" style="left:192px;top:430px;width:40px;height:63px;background:var(--red)"></div>
  </div>

  <div class="panel panel--2 panel--red">
    <div class="flame" role="img" aria-label="Large white flame decoration" style="left:34px;top:252px;width:150px;height:241px;background:linear-gradient(180deg,var(--white) 60%,#fbd2d4 100%)"></div>
  </div>

  <div class="panel panel--3 panel--red-fold">
    <div class="cover-mark"></div>
    <div class="cover-name">ROLVEN</div>
    <div class="cover-title">
      <div class="big">ROLVEN CHICKEN</div>
      <div class="small">CHICKEN, BURGERS,</div>
      <div class="small">KEBABS + PIZZA</div>
    </div>
    <div class="cover-info" style="top:362px;font-size:8px">MINIMUM DELIVERY - <span style="font-size:17px">£9.99</span></div>
    <div class="cover-info" style="top:390px;font-size:8px">WWW.ROLVENCHICKEN.COM</div>
    <div class="cover-info" style="top:410px;font-size:8px">01632 960482</div>
    <div class="flame" role="img" aria-label="Small white flame decoration" style="left:30px;top:425px;width:56px;height:68px;background:var(--white)"></div>
  </div>
</section>

<!-- INSIDE SHEET -->
<section class="sheet sheet--inner">
  <div class="panel panel--1" style="background:linear-gradient(90deg,#ffffff 0%,var(--cream) 70%,var(--mint) 100%)">
    <div class="tag" style="left:20px;top:22px">FRIED CHICKEN</div>
    <div class="abs rule" style="left:20px;top:58px;width:80px;height:48px"></div>
    <div class="row" style="left:27px;top:60px">1&nbsp;&nbsp;&nbsp;&nbsp;piece<span class="p" style="left:44px">1.80 £</span></div>
    <div class="row" style="left:27px;top:72px">2&nbsp;&nbsp;&nbsp;&nbsp;pieces<span class="p" style="left:44px">3.00 £</span></div>
    <div class="row" style="left:27px;top:84px">3&nbsp;&nbsp;&nbsp;&nbsp;pieces<span class="p" style="left:44px">4.10 £</span></div>
    <div class="row" style="left:27px;top:96px">4&nbsp;&nbsp;&nbsp;&nbsp;pieces<span class="p" style="left:44px">5.10 £</span></div>
    <div class="abs rule" style="left:108px;top:58px;width:80px;height:36px"></div>
    <div class="row" style="left:115px;top:60px">5&nbsp;&nbsp;&nbsp;&nbsp;pieces<span class="p" style="left:44px">6.00 £</span></div>
    <div class="row" style="left:115px;top:72px">8&nbsp;&nbsp;&nbsp;&nbsp;pieces<span class="p" style="left:44px">9.00 £</span></div>
    <div class="row" style="left:115px;top:84px">10&nbsp;pieces<span class="p" style="left:44px">11.00 £</span></div>

    <div class="tag" style="left:20px;top:118px">SPICY HOT WINGS</div>
    <div class="abs rule" style="left:20px;top:150px;width:80px;height:36px"></div>
    <div class="row" style="left:27px;top:152px">4&nbsp;&nbsp;&nbsp;&nbsp;piece<span class="p" style="left:44px">2.00 £</span></div>
    <div class="row" style="left:27px;top:164px">6&nbsp;&nbsp;&nbsp;&nbsp;pieces<span class="p" style="left:44px">2.70 £</span></div>
    <div class="row" style="left:27px;top:176px">10 pieces<span class="p" style="left:44px">3.60 £</span></div>

    <div class="tag" style="left:20px;top:198px">BURGERS</div>
    <div class="abs rule" style="left:20px;top:230px;width:180px;height:142px"></div>
    <div class="row" style="left:27px;top:232px">Chicken fillet burger<span class="p" style="left:170px">3.00 £</span></div>
    <div class="row" style="left:27px;top:244px">Grilled chicken fillet burger<span class="p" style="left:170px">3.50 £</span></div>
    <div class="row" style="left:27px;top:256px">Chicken fillet burger with bacon<span class="p" style="left:170px">3.40 £</span></div>
    <div class="row" style="left:27px;top:268px">Chicken fillet burger and hash brown<span class="p" style="left:170px">3.40 £</span></div>
    <div class="row" style="left:27px;top:280px">Hot tender chicken fillet burger<span class="p" style="left:170px">3.00 £</span></div>
    <div class="row" style="left:27px;top:292px">¼ pounder with cheese<span class="p" style="left:170px">3.50 £</span></div>
    <div class="row" style="left:27px;top:304px">¼ pounder with cheese and bacon<span class="p" style="left:170px">3.80 £</span></div>
    <div class="row" style="left:27px;top:316px">½ pounder with cheese<span class="p" style="left:170px">4.50 £</span></div>
    <div class="row" style="left:27px;top:328px">½ pounder with cheese and bacon<span class="p" style="left:170px">4.90 £</span></div>
    <div class="row" style="left:27px;top:340px">Triple burger with cheese<span class="p" style="left:170px">5.40 £</span></div>
    <div class="row" style="left:27px;top:352px">Spicy bean burger<span class="p" style="left:170px">3.00 £</span></div>
    <div class="row" style="left:27px;top:364px">Veggie burger<span class="p" style="left:170px">3.00 £</span></div>

    <div class="tag" style="left:20px;top:380px">SIDE ORDERS</div>
    <div class="sides">
      <div class="col-head" style="left:80px;top:405px">SMALL</div>
      <div class="col-head" style="left:103px;top:405px">LARGE</div>
      <div class="abs rule" style="left:20px;top:412px;width:100px;height:72px"></div>
      <div class="row" style="left:27px;top:414px">Chips (French fries)<span class="p" style="left:53px">1.70 £</span><span class="p" style="left:76px">2.30 £</span></div>
      <div class="row" style="left:27px;top:426px">Cheesy chips<span class="p" style="left:53px">3.00 £</span><span class="p" style="left:76px">3.50 £</span></div>
      <div class="row" style="left:27px;top:438px">Onion rings<span class="p" style="left:76px">3.00 £</span></div>
      <div class="row" style="left:27px;top:450px">Garlic mushrooms<span class="p" style="left:76px">3.00 £</span></div>
      <div class="row" style="left:27px;top:462px">Mozzarella stick<span class="p" style="left:76px">3.00 £</span></div>
      <div class="row" style="left:27px;top:474px">Potato wedges + dip<span class="p" style="left:76px">2.50 £</span></div>
      <div class="abs rule" style="left:123px;top:412px;width:100px;height:72px"></div>
      <div class="row" style="left:129px;top:414px">BBQ beans<span class="p" style="left:78px">1.50 £</span></div>
      <div class="row" style="left:129px;top:426px">Rice<span class="p" style="left:78px">2.50 £</span></div>
      <div class="row" style="left:129px;top:438px">Hummus in pitta with salad<span class="p" style="left:78px">3.00 £</span></div>
      <div class="row" style="left:129px;top:450px">Chips in pitta<span class="p" style="left:78px">3.00 £</span></div>
      <div class="row" style="left:129px;top:462px">Hummus in a tub<span class="p" style="left:78px">1.50 £</span></div>
      <div class="row" style="left:129px;top:474px">Tzatziki<span class="p" style="left:78px">1.50 £</span></div>
    </div>
  </div>

  <div class="panel panel--2" style="background:linear-gradient(90deg,var(--cream) 0%,#ffffff 100%)">
    <div class="tag" style="left:16px;top:24px">BBQ SPARE RIBS</div>
    <div class="abs rule" style="left:18px;top:58px;width:80px;height:24px"></div>
    <div class="row" style="left:25px;top:60px">4&nbsp;&nbsp;&nbsp;&nbsp;pieces<span class="p" style="left:40px">3.50 £</span></div>
    <div class="row" style="left:25px;top:72px">6&nbsp;&nbsp;&nbsp;&nbsp;pieces<span class="p" style="left:40px">4.00 £</span></div>
    <div class="tag" style="left:120px;top:52px">DRINKS</div>
    <div class="abs rule" style="left:122px;top:81px;width:80px;height:24px"></div>
    <div class="row" style="left:129px;top:83px">Cans (330 ml)<span class="p" style="left:52px">0.80 £</span></div>
    <div class="row" style="left:129px;top:95px">Bottles (1.5 ltr)<span class="p" style="left:52px">2.50 £</span></div>

    <div class="tag" style="left:16px;top:98px">GRILLS</div>
    <div class="tag-note" style="left:26px;top:125px">ALL GRILLS COME WITH RICE OR PITTA BREAD<br>AND SALAD SAUCE IN SEPARATE IN CONTAINER</div>
    <div class="col-head" style="left:146px;top:146px">SMALL</div>
    <div class="col-head" style="left:174px;top:145px;font-size:6.4px">LARGE</div>

    <div class="item rule" style="left:18px;top:158px"><div class="name">Lamb doner</div><div class="desc">Specially marinated lamb roasted on an oven spit</div><span class="ps" style="left:145px">5.00 £</span><span class="pl" style="left:172px">6.00 £</span></div>
    <div class="item rule" style="left:18px;top:178px"><div class="name">Chicken doner</div><div class="desc">Specially marinated chicken roasted on an oven spit</div><span class="ps" style="left:145px">6.00 £</span><span class="pl" style="left:172px">7.00 £</span></div>
    <div class="item rule" style="left:18px;top:198px"><div class="name">Lamb shish</div><div class="desc">Cubes of filleted lamb marinated olive oil, herbs, seasoning on a charcoal grill</div><span class="ps" style="left:145px">6.50 £</span><span class="pl" style="left:172px">7.80 £</span></div>
    <div class="item rule" style="left:18px;top:224px"><div class="name">Chicken shish</div><div class="desc">Specially marinated cubes of chicken breast skewered and cooked on a charcoal grill</div><span class="ps" style="left:145px">6.00 £</span><span class="pl" style="left:172px">7.00 £</span></div>
    <div class="item rule" style="left:18px;top:251px"><div class="name">Lamb kofte</div><div class="desc">Minced lamb marinated with a variety of spices and cooked on a charcoal grill</div><span class="ps" style="left:145px">6.00 £</span><span class="pl" style="left:172px">7.00 £</span></div>
    <div class="item rule" style="left:18px;top:279px"><div class="name">Mixed kebab</div><div class="desc">Lamb shish kofta, lamb doner</div><span class="pl" style="left:172px">9.50 £</span></div>
    <div class="item rule" style="left:18px;top:299px"><div class="name">House special</div><div class="desc">Chicken shish, lamb shish, kofta, lamb doner</div><span class="pl" style="left:172px">9.99 £</span></div>
    <div class="item rule" style="left:18px;top:318px"><div class="name">Doner meat and chips <span style="font-size:5px">(lamb doner)</span></div><span class="pl" style="left:172px">6.00 £</span></div>
    <div class="item rule" style="left:18px;top:332px"><div class="name">Doner meat and rice <span style="font-size:5px">(lamb doner)</span></div><span class="pl" style="left:172px">6.00 £</span></div>
    <div class="item rule" style="left:18px;top:346px"><div class="name">Halloumi kebab</div><div class="desc">Halloumi cheese cooked over charcoal grill with onion and tomato</div><span class="pl" style="left:172px">6.00 £</span></div>
    <div class="item rule" style="left:18px;top:372px"><div class="name">Grilled sea bass</div><div class="desc">Grilled sea bass served with chips, special sauce and salad</div><span class="pl" style="left:172px">10.00 £</span></div>
    <div class="item rule" style="left:18px;top:392px"><div class="name">Grilled sea bream</div><div class="desc">Grilled sea bream served with chips, special sauce and salad</div><span class="pl" style="left:172px">10.00 £</span></div>

    <div class="tag" style="left:20px;top:426px">GARLIC BREADS</div>
    <div class="abs rule" style="left:20px;top:456px;width:160px;height:34px"></div>
    <div class="row" style="left:27px;top:458px">Garlic Torpedo<span class="p" style="left:130px">2.50 £</span></div>
    <div class="row" style="left:27px;top:470px">Garlic Torpedo with cheese<span class="p" style="left:130px">3.00 £</span></div>
    <div class="row" style="left:27px;top:482px">Garlic Torpedo with cheese and mushroom<span class="p" style="left:130px">3.50 £</span></div>
  </div>

  <div class="panel panel--3 panel--pale-r">
    <div class="flame" role="img" aria-label="Soft beige flame decoration" style="left:110px;top:300px;width:123px;height:193px;background:linear-gradient(180deg,rgba(232,195,167,.55) 0%,var(--sand) 100%)"></div>
    <div class="flame" role="img" aria-label="Small beige flame decoration" style="left:14px;top:440px;width:36px;height:53px;background:rgba(232,195,167,.7)"></div>

    <div class="abs rule" style="left:14px;top:8px;width:160px;height:38px"></div>
    <div class="row" style="left:20px;top:10px">Garlic Torpedo with cheese and pepperoni<span class="p" style="left:130px">3.80 £</span></div>
    <div class="row" style="left:20px;top:22px">Garlic Torpedo with cheese and jalapeno<span class="p" style="left:130px">3.50 £</span></div>
    <div class="row" style="left:20px;top:34px">Garlic Torpedo with cheese and bacon<span class="p" style="left:130px">3.50 £</span></div>

    <div class="tag" style="left:14px;top:56px">PIZZA MENU</div>
    <div class="tag-note" style="left:30px;top:84px">YOU CAN ALSO CHOOSE WITH BBQ<br>OR GARLIC BASED TOMATO PUREE</div>

    <div class="item rule" style="left:14px;top:110px"><div class="name">1) Margherita</div><div class="desc">Cheese and tomato</div><span class="pl" style="left:182px">5.50 £</span></div>
    <div class="item rule" style="left:14px;top:130px"><div class="name">2) BBQ Lovers</div><div class="desc">BBQ base, chicken, sweetcorn and mix peppers</div><span class="pl" style="left:182px">7.00 £</span></div>
    <div class="item rule" style="left:14px;top:149px"><div class="name">3) Tandoori Hot</div><div class="desc">Chicken, double jalapeno, onion, mushroom</div><span class="pl" style="left:182px">7.00 £</span></div>
    <div class="item rule" style="left:14px;top:169px"><div class="name">4) Hawaiian</div><div class="desc">Ham and pineapple</div><span class="pl" style="left:182px">6.50 £</span></div>
    <div class="item rule" style="left:14px;top:189px"><div class="name">5) Spicy hot one</div><div class="desc">Green chillies, chicken, mix peppers, onion</div><span class="pl" style="left:182px">7.00 £</span></div>
    <div class="item rule" style="left:14px;top:209px"><div class="name">6) Meat feast</div><div class="desc">Salami, pepperoni, ham, beef</div><span class="pl" style="left:182px">7.50 £</span></div>
    <div class="item rule" style="left:14px;top:228px"><div class="name">7) Bacon original</div><div class="desc">Bacon, mushroom, mix pepper, fresh tomato</div><span class="pl" style="left:182px">7.00 £</span></div>
    <div class="item rule" style="left:14px;top:247px"><div class="name">8) Tripple pepperoni</div><div class="desc">Cheese, tomato, triple pepperoni</div><span class="pl" style="left:182px">7.00 £</span></div>
    <div class="item rule" style="left:14px;top:267px"><div class="name">9) Vegetarian</div><div class="desc">Mushroom, mix peppers, onion, sweetcorn, olives</div><span class="pl" style="left:182px">7.00 £</span></div>
    <div class="item rule" style="left:14px;top:287px"><div class="name">10) Doner pizza</div><div class="desc">Lamb doner, onion, jalapeno</div><span class="pl" style="left:182px">7.00 £</span></div>
    <div class="item rule" style="left:14px;top:307px"><div class="name">Create your own</div><span class="ps" style="left:150px">10"</span><span class="pl" style="left:182px">12"</span></div>
    <div class="item rule" style="left:14px;top:321px"><div class="name">Extra toppings</div><div class="desc" style="width:140px">Cheese, tomato, sweetcorn, mushroom, jalapeno, onion, pineapple, mix pepper, chicken, ham, salami, pepperoni, beef, bacon, olives</div><span class="ps" style="left:150px">1.00 £</span><span class="pl" style="left:182px">1.50 £</span></div>

    <div class="tag" style="left:14px;top:356px">DESSERTS</div>
    <div class="abs rule" style="left:14px;top:386px;width:160px;height:60px"></div>
    <div class="row" style="left:20px;top:388px">White chocolate raspberry cheese cake<span class="p" style="left:130px">3.00 £</span></div>
    <div class="row" style="left:20px;top:400px">Chocolate cheese cake<span class="p" style="left:130px">2.50 £</span></div>
    <div class="row" style="left:20px;top:412px">Strawberry cheese cake<span class="p" style="left:130px">2.50 £</span></div>
    <div class="row" style="left:20px;top:424px">Eton mess cheese cake<span class="p" style="left:130px">3.00 £</span></div>
    <div class="row" style="left:20px;top:436px">Chocolate fudge Lumpy Bumpy<span class="p" style="left:130px">3.50 £</span></div>
  </div>
</section>

</body>
</html>
```